Simple Easy - Taekwondo brochure

I have the content and an idea of the layout I want. I need it to look nice and sharp.

It's a sided 8.5x11 colored brochure

please feel free to move things around and use the images provided

my website is www.brolvexia.net if you need an understanding of what the business is about.

all text content is on the website. please be creative!

Target Market(s)

Mothers...must by family friendly because it's for mothers to bring their kids.

Industry/Entity Type

Martial Art

Font styles to use
Other font styles liked:
• Lato

```html
<!DOCTYPE html>
<html lang="en">
<head>
<meta charset="utf-8">
<title>Brolvexia Taekwondo Brochure</title>
<link href="https://fonts.googleapis.com/css2?family=Lato:wght@400;700;900&family=Oswald:wght@500;700&display=swap" rel="stylesheet">
<style>
:root{
  --ink:#0c0e13;
  --navy:#0f1d3a;
  --red:#d4171e;
  --blue:#1e6bc4;
  --gold:#d9b45a;
  --paper:#f4f4f4;
  --text-dark:#222;
  --text-light:#e9e9e9;
  --stage:#e6e6e6;
}
*{margin:0;padding:0;box-sizing:border-box}
html,body{width:765px;height:1200px;overflow:hidden;background:var(--stage);font-family:'Lato',sans-serif}
.spread{position:absolute;left:20px;width:725px;height:560px;display:flex;overflow:hidden;box-shadow:0 3px 10px rgba(0,0,0,.25)}
.spread--outside{top:20px;background:linear-gradient(160deg,#141821 0%,var(--ink) 60%,#0a0b0f 100%)}
.spread--inside{top:620px;background:var(--paper)}
.panel{position:relative;width:33.333%;height:100%;padding:14px 16px}
.swoosh{position:absolute;left:0;width:100%;pointer-events:none}
h2.panel-title{font-family:'Lato',sans-serif;font-weight:400;color:#fff;font-size:11px;letter-spacing:.5px;text-align:center;margin-bottom:8px}
.outside p{color:var(--text-light);font-size:6.4px;line-height:1.35;text-align:justify;margin-bottom:5px}
.portrait{position:absolute;border-radius:50%;border:4px solid #ddd;box-shadow:0 0 0 2px #999}
.awards{position:absolute;left:14px;right:14px;top:400px;text-align:center}
.awards h3{color:var(--gold);font-weight:400;font-size:11px;letter-spacing:.3px}
.awards .sub{color:var(--red);font-size:6px;margin:3px 0 6px}
.awards li{list-style:none;color:var(--text-light);font-size:6.3px;line-height:1.3;margin-bottom:7px}
.follow{position:absolute;left:0;right:0;bottom:14px;text-align:center;color:var(--red);font-size:5.5px}
.follow span{display:inline-block;width:9px;height:9px;border-radius:50%;background:var(--blue);vertical-align:middle;margin-left:2px}
.quote-name{color:var(--red);font-style:italic;font-size:8px;text-align:center;margin:4px 0 10px}
.map{position:absolute;left:72px;top:330px;width:96px;height:96px;border-radius:50%;border:3px solid #ccc;background:radial-gradient(circle at 50% 45%,#f1efe9,#d8d6cf)}
.contact{position:absolute;left:0;right:0;top:438px;text-align:center;color:#fff}
.contact .keep{font-size:8px;font-weight:700;margin-bottom:9px}
.contact .name{font-size:9px;font-weight:900;color:var(--red);letter-spacing:.3px}
.contact .addr{font-size:6.8px;margin:5px 0}
.contact .call{font-size:8.5px;letter-spacing:.5px}
.contact .phone{font-size:15px;font-weight:900;margin:2px 0}
.contact .web{font-size:6.5px;color:var(--blue);letter-spacing:1px}
.offer-photo{position:absolute;left:0;top:0;width:100%;height:320px;background:radial-gradient(ellipse at 40% 55%,#2a4d86 0%,#16284a 35%,#0a0e18 75%)}
.offer{position:absolute;left:0;right:0;top:14px;text-align:center;color:#fff}
.offer .label{font-size:11px;letter-spacing:.5px}
.offer .pct{font-family:'Oswald',sans-serif;font-weight:700;font-size:58px;color:var(--gold);line-height:1;margin-top:2px;display:inline-block}
.offer .off{font-family:'Oswald',sans-serif;font-weight:700;font-size:16px;color:var(--gold);display:inline-block;writing-mode:vertical-rl;transform:rotate(180deg);vertical-align:top;margin-top:8px}
.offer .note{font-size:6.5px;letter-spacing:.2px}
.brand{position:absolute;left:0;right:0;top:368px;text-align:center}
.brand .mark{display:inline-block;width:60px;height:60px;border-radius:50%;background:var(--blue);margin-bottom:12px}
.brand .name{font-weight:900;color:#fff;font-size:24px;line-height:1.05;letter-spacing:.5px}
.brand .tagline{color:var(--blue);font-size:8.5px;letter-spacing:1px;margin-top:8px}
.brand .web{color:#fff;font-size:7px;letter-spacing:1px;margin-top:12px}

.inside p{color:var(--text-dark);font-size:6.7px;line-height:1.38;text-align:justify;margin-bottom:6px}
.mascot{position:absolute;left:70px;top:24px;width:100px;height:92px;border-radius:50%;background:radial-gradient(circle,#f3a64a 0%,#e07a2a 55%,rgba(224,122,42,0) 72%)}
.intro{position:absolute;left:20px;right:20px;top:122px;text-align:center;font-size:8.5px;color:var(--text-dark);line-height:1.25}
.benefits{position:absolute;left:10px;right:10px;top:160px;display:grid;grid-template-columns:repeat(3,1fr);row-gap:12px;text-align:center}
.benefit i{display:block;width:18px;height:18px;border-radius:50%;background:var(--blue);margin:0 auto 4px}
.benefit:nth-child(3n+1) i{background:#2050a0}
.benefit span{font-size:8px;color:var(--text-dark);font-weight:700}
.pill{display:inline-block;color:#fff;font-weight:900;font-size:10.5px;padding:3px 10px;border-radius:4px;letter-spacing:.3px}
.pill--red{background:var(--red)}
.pill--blue{background:var(--blue)}
.policy{position:absolute;left:22px;right:22px;text-align:center}
.policy p{text-align:center;margin-top:6px;font-size:6.9px}
.tenets-title{font-family:'Oswald',sans-serif;font-weight:700;color:var(--red);font-size:20px;text-align:center;margin:10px 0 8px;letter-spacing:.3px}
.tenet{text-align:center;margin-bottom:6px}
.tenet .pill{font-size:9.5px;padding:2px 16px;margin-bottom:6px}
.tenet p{text-align:justify}
.coach{position:absolute;left:66px;top:256px;width:110px;height:110px;background:radial-gradient(circle,#3b3d44,#111)}
.coach-quote{position:absolute;left:16px;right:16px;top:384px}
.footer{position:absolute;left:0;right:0;bottom:12px;text-align:center;color:#fff;font-size:7.5px;letter-spacing:1px}
.footer em{font-style:normal;color:var(--red)}
</style>
</head>
<body>

<!-- Outside spread -->
<section class="spread spread--outside outside">
  <svg class="swoosh" style="top:330px;height:120px" viewBox="0 0 725 120" preserveAspectRatio="none">
    <path d="M0 70 C180 20 420 10 725 55" stroke="#d4171e" stroke-width="5" fill="none"/>
    <path d="M0 80 C190 32 430 22 725 66" stroke="#1e6bc4" stroke-width="2.5" fill="none"/>
  </svg>

  <div class="panel">
    <h2 class="panel-title">MASTER DAN</h2>
    <p>Daniel Orrin (Master Dan) is the owner and head instructor at Brolvexia Taekwondo. Master Dan is a Halvorn-certified 3rd degree Black Belt. The Halvorn Institute is the overseeing authority of all Black Belts in the world, working with the World Sparring Federation (WSF); it also oversees taekwondo in the Olympics.</p>
    <p>In 1992, at the age of 8, Master Dan began training under Grand Master Velloro who achieved the level of 8th Dan in taekwondo under the International Forms Federation (IFF). The IFF is another highly respected global authority for taekwondo.</p>
    <p>When Master Dan entered Middle School and then High School, his years of taekwondo training became invaluable as he participated in wrestling, track, and hockey.</p>
    <p>In 2013, Master Dan began training under Grand Master Tarn, a 9th Dan in Taekwondo, certified by the Halvorn Institute. Master Dan currently trains under Grand Master Tarn.</p>
    <div class="portrait" role="img" aria-label="Portrait photo of Master Dan" style="left:50px;top:238px;width:140px;height:140px;background:radial-gradient(circle,#f6f6f6,#cfcfcf)"></div>
    <div class="awards">
      <h3>AWARDS / ACHIEVEMENTS</h3>
      <div class="sub">(under Master Dan's leadership)</div>
      <ul>
        <li>4 National Taekwondo Union Championships / WSF sanctioned</li>
        <li>10 State Medalists National Taekwondo Union State Championships / WSF sanctioned</li>
        <li>12 Eastern Collegiate Martial Arts League (ECML) Team Medals / WSF sanctioned</li>
        <li>1 Eastern Collegiate Martial Arts League (ECML) TOP DIVISION TEAM TITLES / WSF sanctioned</li>
      </ul>
    </div>
    <div class="follow">Follow Us : <span></span><span></span><span></span></div>
  </div>

  <div class="panel">
    <h2 class="panel-title">TESTIMONIAL</h2>
    <p>“ I started taking classes with Master Dan a little over 3 years ago. As the newest member of the class, I was shy and unsure of myself. However, I quickly overcame those feelings because Master Dan is a natural teacher. Paired with his passion for the sport, his gift for teaching makes him one of the best coaches I have encountered. I have seen him work with both children and adults and his manner is unfailingly supportive and encouraging. As a teacher myself, I see how he tailors his teaching style to each student and I hope to follow his example in my classroom. I am thankful that my first experience with taekwondo has been through Master Dan's class. ”</p>
    <div class="quote-name">- RENEE T.</div>
    <p>“ I have been training with Master Dan for the past 6 years, and as a teenager who yearns for vigorous training, I have not been disappointed. For the first 3 years of my taekwondo career, I have been to different dojangs, but I decided to settle for Brolvexia Taekwondo for several reasons. Master Dan is an instructor who is very understanding of every student's specific needs, and gives the attention needed to each student. His care for his students transcends just taekwondo, and he is a very patient and understanding man. At the end of a taekwondo class, there is a certain satisfaction in sweating after training, and Master Dan does not fail to achieve that for its students! ”</p>
    <div class="quote-name">- MARCUS D.</div>
    <div class="map" role="img" aria-label="Street map showing the school location"></div>
    <div class="contact">
      <div class="keep">Keep in Touch</div>
      <div class="name">BROLVEXIA TAEKWONDO</div>
      <div class="addr">2875 Linden Row, Harlow Meadow, PA, 19088</div>
      <div class="call">CALL US TODAY !</div>
      <div class="phone">(555) 014-2291</div>
      <div class="web">www.brolvexia.net</div>
    </div>
  </div>

  <div class="panel">
    <div class="offer-photo" role="img" aria-label="Photo of a student tying a blue belt"></div>
    <div class="offer">
      <div class="label">SPECIAL OFFER</div>
      <div><span class="pct">50%</span><span class="off">OFF</span></div>
      <div class="note">TRIAL LESSIONS &amp; GET A FREE T-SHIRT</div>
    </div>
    <div class="brand">
      <div class="mark"></div>
      <div class="name">BROLVEXIA<br>TAEKWONDO</div>
      <div class="tagline">FOCUS YOUR CHILD'S POTENTIAL</div>
      <div class="web">www.brolvexia.net</div>
    </div>
  </div>
</section>

<!-- Inside spread -->
<section class="spread spread--inside inside">
  <svg class="swoosh" style="top:0;height:24px" viewBox="0 0 725 24" preserveAspectRatio="none">
    <path d="M10 8 C100 2 180 4 240 12 L240 16 C180 8 100 7 10 12Z" fill="#d4171e"/>
    <path d="M485 14 C560 6 640 4 715 8 L715 12 C640 9 560 10 485 18Z" fill="#d4171e"/>
  </svg>
  <svg class="swoosh" style="bottom:0;height:100px" viewBox="0 0 725 100" preserveAspectRatio="none">
    <path d="M0 30 C250 52 480 50 725 24 L725 100 L0 100Z" fill="#101114"/>
    <path d="M0 26 C250 46 480 44 725 20" stroke="#d4171e" stroke-width="3" fill="none"/>
  </svg>

  <div class="panel">
    <div class="mascot" role="img" aria-label="Cartoon tiger mascot holding a belt"></div>
    <div class="intro">Brolvexia Taekwondo is the perfect tool to unlocking your child's protential.</div>
    <div class="benefits">
      <div class="benefit"><i></i><span>Discipline</span></div>
      <div class="benefit"><i></i><span>Self-Defense</span></div>
      <div class="benefit"><i></i><span>Focus</span></div>
      <div class="benefit"><i></i><span>Self-Respect</span></div>
      <div class="benefit"><i></i><span>Leadership</span></div>
      <div class="benefit"><i></i><span>Anti-Bullying</span></div>
    </div>
    <div class="policy" style="top:298px">
      <span class="pill pill--red">NO CONTRACTS!</span>
      <p>There are NO contracts at Brolvexia Taekwondo. We believe that the relationship established with each student is extremely important.</p>
    </div>
    <div class="policy" style="top:374px">
      <span class="pill pill--blue">NO EXTRA FEES!</span>
      <p>At Brolvexia Taekwondo, there are NO enrollment fees, belt rank fees, testing fees (until Black Belt), or cancellation fees, if a student stops their training.</p>
    </div>
    <div class="footer">www.brolvexia.net</div>
  </div>

  <div class="panel" style="background:#ececec">
    <h2 class="tenets-title">THE FIVE TENETS</h2>
    <div class="tenet"><span class="pill pill--red">COURTESY</span>
      <p>Students will show courtesy to all others in the dojang, as well as people they meet outside of their formal training.</p>
      <p>Younger students will address adults as “Sir” or “Ma'am.”</p></div>
    <div class="tenet"><span class="pill pill--blue">INTEGRITY</span>
      <p>Students are expected to be honest and be willing to exhibit strong moral principles that will help them distinguish between right and wrong.</p></div>
    <div class="tenet"><span class="pill pill--red">PERSEVERANCE</span>
      <p>Students must remember that they will never grow stronger by engaging their doubts. Therefore, students should be willing to confront their fears, battle back against their struggles, and never look for short-cuts when achieving their goals.</p></div>
    <div class="tenet"><span class="pill pill--blue">SELF -CONTROL</span>
      <p>Students are expected to keep their emotions (thoughts and actions) in-check at all times, both inside and outside the dojang.</p></div>
    <div class="tenet"><span class="pill pill--red">INDOMITABLE SPIRIT</span>
      <p>Students will consistently exhibit a full 100% effort in all they do inside and outside the dojang.</p>
      <p>Students must show courage when standing up for their beliefs and convictions inside and outside the dojang.</p></div>
    <div class="footer"><em>Call Us Today!</em> (555) 014-2291</div>
  </div>

  <div class="panel">
    <div style="margin-top:16px">
      <p>It is important that the original master and creator of a school's curriculum remains the head instructor. This is to ensure that the details of each student's growth process are not compromised.</p>
      <p>When looking for a martial arts school, it can be difficult as to what you are looking for. We live in an age of commercialized, franchised martial arts and a market saturated with instructors who do not fully understand the arts.</p>
      <p>This is driven by test fees and extra costs because it gives schools another way to charge you, which becomes a problem when they are simply promoting students for extra income rather than promoting based on development and understanding.</p>
      <p>At Brolvexia Taekwondo, we test on a firm but fair system to ensure that we do not add to the problem and do not become belt factories.</p>
    </div>
    <div class="portrait coach" role="img" aria-label="Portrait photo of Master Dan in uniform"></div>
    <div class="coach-quote">
      <p>“ Brolvexia Taekwondo is more than just “training” for strength, speed, and power; a student's character, integrity, confidence, and self-esteem can only be improved by coaching each student personally and helping them achieve their goals. I want students to feel that the time they've spent at Brolvexia Taekwondo has not only benefited them physically, but has also improved their lives. ”</p>
    </div>
    <div class="footer">www.brolvexia.net</div>
  </div>
</section>

</body>
</html>
```